Wellness Wordpress Blog Redesign

I am looking to redesign by wordpress blog - www.MarnieCollardActive.com. I would like to have a more personalized feel that resonates with my brand of Renewed Balance through fitness, nutrition, self care and self love. I'd like capabilities to do the following:

Ideally, I'd like to have the home page feature not only my latest blog posts or videos, but to also include a place to click to learn more about other facets of my business.

Ideally, I'd love to have a page layout of:

Home - main page to host key features of the brand & latest blog posts
About - Place to learn more about me and my brand
Blog -
Fitness - Host some videos and fitness tips and links to resources
Nutrition - Host some videos and recipes and links to resources
Self Care - Host some videos and self care tips and links to resources
Shop - Host a video (that can be changed of the product of the month) and links to other resources

Number of Pages Required

5+ page

Font styles to use
Serif
Decorative

Colors
85acd3
0393ce
00a990
6b449b
a64599
b8a6cd

Requirements
Must have
• Home - main page to host key features of the brand & latest blog posts
• About - Place to learn more about me and my brand
• Blog -
• Fitness - Host some videos and fitness tips and links to resources
• Nutrition - Host some videos and recipes and links to resources
• Self Care - Host some videos and self care tips and links to resources
• Shop - Host a video (that can be changed of the product of the month) and links to other resources
• Video / Mutlimedia capabilities
Nice to have
• Option to have a calendar of events widgets for people to sign up for events that I'm hosting

```html
<!DOCTYPE html>
<html lang="en">
<head>
<meta charset="utf-8">
<title>Marnie Collard Active</title>
<link rel="stylesheet" href="https://fonts.googleapis.com/css2?family=Raleway:wght@500;600;700&family=Open+Sans:wght@400;600;700&display=swap">
<style>
:root{
  --purple:#9a2f8f;
  --purple-dark:#7d2a86;
  --blue:#1b7fc4;
  --teal:#16977b;
  --cal-blue:#1f7dc1;
  --cal-light:#dde9f4;
  --ink:#1a1a1a;
  --text:#555;
  --line:#d6d6d6;
  --footer:#0d0d0d;
  --green:#2a9a3a;
  --red:#d52a2a;
}
*{box-sizing:border-box;margin:0;padding:0}
html,body{width:1200px;height:3888px;overflow:hidden}
body{background:#fff;font-family:"Open Sans",Arial,sans-serif;color:var(--text);position:relative}
.abs{position:absolute}
h1,h2,h3,h4{font-family:"Raleway",Arial,sans-serif;color:var(--ink)}

/* header */
.site-header{top:0;left:0;width:1200px;height:98px}
.brand{left:96px;top:18px;display:flex;align-items:center;gap:14px}
.brand-mark{width:14px;height:14px;border-radius:50%;background:var(--purple)}
.brand-name{font-family:"Raleway",sans-serif;font-weight:700;font-size:34px;color:var(--purple);line-height:58px}
.main-nav{right:96px;top:0;height:98px;display:flex;align-items:center;gap:28px;font-family:"Raleway",sans-serif;font-weight:600;font-size:17px;color:var(--ink)}
.main-nav .active{color:var(--purple)}

/* hero */
.hero{top:98px;left:0;width:1200px;height:537px;background:linear-gradient(100deg,#3f5a26 0%,#55712f 40%,#7a8f3a 65%,#5d7a2a 100%)}
.hero-title{left:98px;top:132px;font-family:"Raleway",sans-serif;font-weight:700;font-size:39px;line-height:57px;color:#fff;width:640px}
.btn-outline{left:98px;top:340px;width:196px;height:57px;border:2px solid #fff;border-radius:30px;color:#fff;font-family:"Raleway",sans-serif;font-weight:700;font-size:14px;display:flex;align-items:center;justify-content:center;letter-spacing:.5px}
.hero-dots{left:568px;top:458px;display:flex;gap:6px}
.hero-dots span{width:13px;height:13px;border-radius:50%;border:2px solid #fff}
.hero-dots span:first-child{background:#fff}

/* welcome */
.section-title{width:1200px;text-align:center;font-weight:600;font-size:38px;left:0}
.intro{left:200px;width:800px;text-align:center;font-size:13px;line-height:26px}
.pillar{width:300px;text-align:center}
.pillar-icon{width:200px;height:200px;border-radius:50%;margin:0 auto;display:flex;align-items:center;justify-content:center;border:9px solid #fff;box-shadow:0 0 0 5px currentColor}
.pillar h3{margin-top:52px;font-weight:700;font-size:21px}
.pillar p{margin-top:22px;font-size:13px;line-height:26px}

/* what we do */
.what-box{left:0;top:1381px;width:666px;height:407px;border:2px solid var(--line);border-left:none}
.what-title{left:130px;top:1422px;font-weight:600;font-size:38px}
.what-text{left:130px;top:1485px;width:460px;font-size:13px;line-height:26px}
.what-text p+p{margin-top:20px}
.btn-purple{left:132px;top:1700px;width:132px;height:46px;border-radius:24px;background:var(--purple-dark);color:#fff;font-family:"Raleway",sans-serif;font-weight:700;font-size:13px;display:flex;align-items:center;justify-content:center}
.video{left:619px;top:1423px;width:482px;height:321px;background:linear-gradient(120deg,#1e2226,#3d454c 50%,#23282d)}
.play{left:830px;top:1555px}

/* newsletter */
.newsletter{left:0;top:1897px;width:1200px;height:389px;background:linear-gradient(100deg,#9a2f86 0%,#6b4aa0 45%,#2d7cc7 100%)}
.newsletter h2{position:absolute;top:70px;width:1200px;text-align:center;color:#fff;font-weight:600;font-size:38px}
.newsletter p{position:absolute;top:138px;left:260px;width:680px;text-align:center;color:#fff;font-size:13px;line-height:26px}
.email{position:absolute;left:280px;top:233px;width:497px;height:57px;background:#fff;font-size:15px;color:#666;padding-left:24px;display:flex;align-items:center}
.subscribe{position:absolute;left:777px;top:233px;width:143px;height:57px;background:var(--purple);color:#fff;font-family:"Raleway",sans-serif;font-weight:700;font-size:15px;display:flex;align-items:center;justify-content:center}

/* calendar */
.cal-photo{left:98px;top:2470px;width:358px;height:420px;background:linear-gradient(160deg,#4a4a4a,#2c2c2c 60%,#3b3b3b)}
.calendar{left:456px;top:2470px;width:645px;border-collapse:collapse;table-layout:fixed;font-size:14px}
.calendar td,.calendar th{border:1px solid #c9d3dc;height:56px;text-align:center;vertical-align:middle;color:#555}
.calendar .month th{background:var(--cal-blue);color:#fff;height:42px;font-family:"Raleway",sans-serif;font-size:18px;font-weight:700;border-color:var(--cal-blue)}
.calendar .month .arrow{font-size:16px}
.calendar .days th{height:42px;font-weight:700;color:var(--ink);font-size:15px;background:#fff}
.calendar .shade td{background:var(--cal-light)}
.calendar .day{display:block;font-size:14px}
.tag{display:block;font-size:10px;font-weight:700;line-height:12px}
.booked{color:var(--red)}
.available{color:var(--green)}
.divider{left:98px;top:2965px;width:1004px;height:2px;background:var(--line)}

/* blog */
.post{top:3136px;width:324px}
.post-img{width:324px;height:208px}
.post h4{margin-top:34px;font-weight:600;font-size:20px}
.meta{margin-top:12px;font-size:11px;color:#666;display:flex;align-items:center;gap:6px}
.meta svg{flex:none}
.excerpt{margin-top:10px;font-size:12px;line-height:22px}
.read{margin-top:20px;font-family:"Raleway",sans-serif;font-weight:700;font-size:13px;color:var(--purple)}

/* footer */
.site-footer{left:0;top:3611px;width:1200px;height:277px;background:var(--footer);color:#fff}
.contact{position:absolute;top:70px;display:flex;align-items:center;gap:16px;font-size:14px;line-height:22px}
.contact .ring{width:44px;height:44px;border-radius:50%;border:2px solid #2a8bd0;display:flex;align-items:center;justify-content:center}
.footer-nav{position:absolute;top:142px;width:1200px;text-align:center;font-size:15px}
.footer-nav span{margin:0 20px}
.copyright{position:absolute;left:98px;top:226px;font-size:12px}
.social{position:absolute;right:98px;top:212px;display:flex;gap:12px}
.social span{width:40px;height:40px;border-radius:50%;border:2px solid #fff}
</style>
</head>
<body>

<header class="abs site-header">
  <div class="abs brand"><span class="brand-mark"></span><span class="brand-name">Marnie Collard</span></div>
  <nav class="abs main-nav">
    <span class="active">Home</span><span>About</span><span>Blog</span><span>Fitness</span><span>Nutrition</span><span>Selfcare</span><span>Shop</span><span>Contact us</span>
    <svg width="16" height="16" viewBox="0 0 16 16"><circle cx="6.5" cy="6.5" r="5" fill="none" stroke="#1a1a1a" stroke-width="2"/><line x1="10" y1="10" x2="15" y2="15" stroke="#1a1a1a" stroke-width="2.4"/></svg>
  </nav>
</header>

<section class="abs hero" role="img" aria-label="Photo of a smiling couple running together on a sunny wooded park path"></section>
<h1 class="abs hero-title">Sharing My Passion for Health, Fitness &amp; Self Care to Help You Live Your Best Life</h1>
<div class="abs btn-outline">GET MORE INFO</div>
<div class="abs hero-dots"><span></span><span></span><span></span><span></span></div>

<h2 class="abs section-title" style="top:720px">WELCOME TO MARNIE COLLARD ACTIVE</h2>
<p class="abs intro" style="top:795px">Nemo enim ipsam voluptatem quia voluptas sit aspernatur aut odit aut fugit, sed quia consequuntur magni dolores eos qui ratione voluptatem sequi nesciunt. Neque porro quisquam est, qui dolorem ipsum quia dolor sit amet, consectetur, adipisci velit, sed quia non numquam eius modi tempora incidunt ut labore et dolore magnam aliqua</p>

<div class="abs pillar" style="left:96px;top:920px">
  <div class="pillar-icon" style="background:var(--blue);color:var(--blue)">
    <svg width="84" height="76" viewBox="0 0 24 22"><path d="M12 21 2.5 11.6C-.4 8.7.6 3.4 4.7 2.2 7.4 1.4 10 2.6 12 5c2-2.4 4.6-3.6 7.3-2.8 4.1 1.2 5.1 6.5 2.2 9.4Z" fill="#fff"/></svg>
  </div>
  <h3>HEALTH</h3>
  <p>Nam libero tempore, cum soluta nobis est eligendi optio cumque nihil impedit quo minus id quod maxpoime placeat face.</p>
</div>
<div class="abs pillar" style="left:446px;top:920px">
  <div class="pillar-icon" style="background:var(--teal);color:var(--teal)">
    <svg width="110" height="50" viewBox="0 0 44 20"><rect x="0" y="7" width="4" height="6" fill="#fff"/><rect x="5" y="2" width="5" height="16" rx="1" fill="#fff"/><rect x="11" y="4" width="4" height="12" rx="1" fill="#fff"/><rect x="15" y="8.5" width="14" height="3" fill="#fff"/><rect x="29" y="4" width="4" height="12" rx="1" fill="#fff"/><rect x="34" y="2" width="5" height="16" rx="1" fill="#fff"/><rect x="40" y="7" width="4" height="6" fill="#fff"/></svg>
  </div>
  <h3>FITNESS</h3>
  <p>Nam libero tempore, cum soluta nobis est eligendi optio cumque nihil impedit quo minus id quod maxpoime placeat face.</p>
</div>
<div class="abs pillar" style="left:801px;top:920px">
  <div class="pillar-icon" style="background:var(--purple);color:var(--purple)">
    <svg width="70" height="74" viewBox="0 0 20 21"><circle cx="10" cy="5.5" r="5" fill="#fff"/><path d="M1 21v-3c0-3.5 3-6 6-6h6c3 0 6 2.5 6 6v3Z" fill="#fff"/></svg>
  </div>
  <h3>SELF CARE</h3>
  <p>Nam libero tempore, cum soluta nobis est eligendi optio cumque nihil impedit quo minus id quod maxpoime placeat face.</p>
</div>

<div class="abs what-box"></div>
<h2 class="abs what-title">WHAT WE DO</h2>
<div class="abs what-text">
  <p>Nam libero tempore, cum soluta nobis est eligendi optio cumque nihil impedit quo minus id quod maxime place.</p>
  <p>Facere possimus, omnis voluptas assumenda est, omnis dolor repellendus emporibus autem quibusdam et aut officiis debitis aut rerum necessitatib us saepe eveniet ut et voluptates repudiandae sint et molestiae non recus and argue earum rerum hic ten.</p>
</div>
<div class="abs btn-purple">READ MORE</div>
<div class="abs video" role="img" aria-label="Video still of a man running on a treadmill in a gym"></div>
<svg class="abs play" width="60" height="60" viewBox="0 0 60 60"><circle cx="30" cy="30" r="29" fill="#000" stroke="#fff" stroke-width="2"/><path d="M24 18 42 30 24 42Z" fill="#fff"/></svg>

<section class="abs newsletter">
  <h2>SIGN UP TO OUR NEWSLETTER</h2>
  <p>Nam libero tempore, cum soluta nobis est eligendi optio cumque nihil impedit quo minus id quod maxime placeat facere possimus, omnis voluptas assumenda est mnis do</p>
  <div class="email">Email Address</div>
  <div class="subscribe">SUBSCRIBE</div>
</section>

<h2 class="abs section-title" style="top:2374px">EVENT CALENDAR</h2>
<div class="abs cal-photo" role="img" aria-label="Photo of a smiling woman lifting a small purple dumbbell"></div>
<table class="abs calendar">
  <tr class="month"><th class="arrow">&#9664;</th><th colspan="5">JUL 2018</th><th class="arrow">&#9654;</th></tr>
  <tr class="days"><th>SUN</th><th>MON</th><th>TUE</th><th>WED</th><th>THU</th><th>FRI</th><th>SAT</th></tr>
  <tr><td></td><td></td><td></td><td></td><td></td><td></td><td>1</td></tr>
  <tr class="shade"><td>2</td><td>3</td><td>4</td><td>5</td><td>6</td><td>7</td><td>8</td></tr>
  <tr><td><span class="tag booked">BOOKED</span><span class="day">9</span></td><td>10</td><td><span class="tag available">&#10004; AVAILABLE</span><span class="day">11</span></td><td>12</td><td>13</td><td><span class="tag booked">BOOKED</span><span class="day">14</span></td><td>15</td></tr>
  <tr class="shade"><td><span class="tag available">&#10004; AVAILABLE</span><span class="day">16</span></td><td>17</td><td>18</td><td><span class="tag booked">BOOKED</span><span class="day">19</span></td><td><span class="tag available">&#10004; AVAILABLE</span><span class="day">20</span></td><td><span class="tag available">&#10004; AVAILABLE</span><span class="day">21</span></td><td>22</td></tr>
  <tr><td>23</td><td><span class="tag booked">BOOKED</span><span class="day">24</span></td><td>25</td><td><span class="tag available">&#10004; AVAILABLE</span><span class="day">26</span></td><td>27</td><td>28</td><td>29</td></tr>
  <tr class="shade"><td>30</td><td>31</td><td></td><td></td><td></td><td></td><td></td></tr>
</table>
<div class="abs divider"></div>

<h2 class="abs section-title" style="top:3042px">LATEST BLOG</h2>
<article class="abs post" style="left:98px">
  <div class="post-img" role="img" aria-label="Photo of a woman with arms raised by a lake at sunrise" style="background:linear-gradient(180deg,#8fb3cf,#c9b48a 60%,#4d5a3c)"></div>
  <h4>Finibus Bonorum et Malorum</h4>
  <div class="meta"><svg width="11" height="11" viewBox="0 0 11 11"><rect x=".5" y="1.5" width="10" height="9" fill="none" stroke="#1b7fc4"/><rect x=".5" y="1.5" width="10" height="3" fill="#1b7fc4"/></svg>25/09/2017 &nbsp;| <svg width="10" height="11" viewBox="0 0 10 11"><circle cx="5" cy="3" r="2.6" fill="#1b7fc4"/><path d="M0 11c0-3 2-5 5-5s5 2 5 5Z" fill="#1b7fc4"/></svg>Dana</div>
  <p class="excerpt">Nemo enim ipsam voluptatem quia volupta asperna tur aut odit aut fugit, sed quia conseq</p>
  <div class="read">READ MORE</div>
</article>
<article class="abs post" style="left:438px">
  <div class="post-img" role="img" aria-label="Photo of running feet on a treadmill in warm light" style="background:linear-gradient(180deg,#e9d6a8,#c29b62 55%,#3e3a36)"></div>
  <h4>Finibus Bonorum et Malorum</h4>
  <div class="meta"><svg width="11" height="11" viewBox="0 0 11 11"><rect x=".5" y="1.5" width="10" height="9" fill="none" stroke="#1b7fc4"/><rect x=".5" y="1.5" width="10" height="3" fill="#1b7fc4"/></svg>25/09/2017 &nbsp;| <svg width="10" height="11" viewBox="0 0 10 11"><circle cx="5" cy="3" r="2.6" fill="#1b7fc4"/><path d="M0 11c0-3 2-5 5-5s5 2 5 5Z" fill="#1b7fc4"/></svg>Dana</div>
  <p class="excerpt">Nemo enim ipsam voluptatem quia volupta asperna tur aut odit aut fugit, sed quia conseq</p>
  <div class="read">READ MORE</div>
</article>
<article class="abs post" style="left:778px">
  <div class="post-img" role="img" aria-label="Photo of a healthy salad bowl surrounded by fresh vegetables" style="background:linear-gradient(135deg,#6e4a2e,#a8743d 45%,#7c8f3a 70%,#5a3b26)"></div>
  <h4>Finibus Bonorum et Malorum</h4>
  <div class="meta"><svg width="11" height="11" viewBox="0 0 11 11"><rect x=".5" y="1.5" width="10" height="9" fill="none" stroke="#1b7fc4"/><rect x=".5" y="1.5" width="10" height="3" fill="#1b7fc4"/></svg>25/09/2017 &nbsp;| <svg width="10" height="11" viewBox="0 0 10 11"><circle cx="5" cy="3" r="2.6" fill="#1b7fc4"/><path d="M0 11c0-3 2-5 5-5s5 2 5 5Z" fill="#1b7fc4"/></svg>Dana</div>
  <p class="excerpt">Nemo enim ipsam voluptatem quia volupta asperna tur aut odit aut fugit, sed quia conseq</p>
  <div class="read">READ MORE</div>
</article>

<footer class="abs site-footer">
  <div class="contact" style="left:158px">
    <span class="ring"><svg width="14" height="18" viewBox="0 0 14 18"><path d="M7 17S1 10 1 6.5a6 6 0 0 1 12 0C13 10 7 17 7 17Z" fill="none" stroke="#2a8bd0" stroke-width="1.8"/><circle cx="7" cy="6.5" r="2" fill="#2a8bd0"/></svg></span>
    <span>218 Larkspur Lane, 4th Floor<br>Portland, OR 97205</span>
  </div>
  <div class="contact" style="left:470px">
    <span class="ring"><svg width="16" height="16" viewBox="0 0 16 16"><path d="M3 1h3l1.5 4-2 1.3a9 9 0 0 0 4.2 4.2L11 8.5l4 1.5v3c0 1-1 2-2 2C7 15 1 9 1 3c0-1 1-2 2-2Z" fill="#2a8bd0"/></svg></span>
    <span>+1 555 014 2290</span>
  </div>
  <div class="contact" style="left:696px">
    <span class="ring"><svg width="16" height="12" viewBox="0 0 16 12"><rect width="16" height="12" rx="1" fill="#2a8bd0"/><path d="M1 1l7 5 7-5" fill="none" stroke="#0d0d0d" stroke-width="1.4"/></svg></span>
    <span>hello@marniecollardactive.com</span>
  </div>
  <div class="footer-nav"><span>About</span>|<span>Media</span>|<span>My Faves</span>|<span>Resources</span>|<span>Services</span></div>
  <div class="copyright">Copyrights © 2018, Marnie Collard Active. All rights reserved.</div>
  <div class="social"><span></span><span></span><span></span><span></span></div>
</footer>

</body>
</html>
```